当社 ㈱セキレイワークスの年賀状(デザイン面のみ)です。
400枚余りをクライアントや雑誌社等の媒体、広告代理店、印刷会社など取引先に送ります。ハガキサイズ(148×100㎜)。特色2色刷。デザインは自由です。あくまで参考ですが、これまでの年賀状の抜粋を添付します。加えて当社のロゴデータを添付します。
明けましておめでとうございます。
創業以来四半世紀に及ぶ活動を礎に、また新たな第一歩を踏み出しました。
これからも、アグレッシブに、元気に、正しきことに労を惜しまず、日々
挑戦し続けます。本年も更に皆様のお役に立てる存在を目指し精進致します。
株式会社セキレイワークス
代表取締役会長 ●●●● 代表取締役社長 ●●●● 社員一同

※基本的に上記の挨拶文を入れていただきますが、これを入れない案(過去年賀状をご参照)もOKです。(その場合、挨拶文はポスト面に入れます。ポスト面のデザインは不要です。)
当社ホームページ
http://www.sekirei-works.example/

ファッションの広告宣伝を取り扱うという当社の業務内容を意識して頂いたこと。
これまでの当社の年賀状と少し違った見え方のデザイン。
巧みな2色での表現。
デザインが上品でまとまっていること。
これらの理由から選択させて頂きました。

この度は多くのご提案を頂きましてありがとうございました。
どの案も素晴らしく、それぞれ個性のある提案であったため、決定に時間が掛かってしまったことをお詫びします。
また、別案件でご相談させて頂く際はよろしくお願いいたします。

```html
<!DOCTYPE html>
<html lang="ja">
<head>
<meta charset="utf-8">
<title>年賀状 — 株式会社セキレイワークス</title>
<link rel="stylesheet" href="https://fonts.googleapis.com/css2?family=Shippori+Mincho:wght@500;700;800&display=swap">
<style>
  :root {
    --ground-red: #8a1b25;
    --ink-red: #9c1f2a;
    --paper: #ffffff;
    --silhouette: #1c1012;
  }
  html, body {
    margin: 0;
    padding: 0;
    overflow: hidden;
    background: var(--ground-red);
  }
  .card {
    position: relative;
    width: 811px;
    height: 1200px;
    overflow: hidden;
    background: var(--ground-red);
    font-family: "Shippori Mincho", serif;
    color: var(--ink-red);
  }
  .sun {
    position: absolute;
    left: calc(405px - 432px);
    top: 136px;
    width: 864px;
    height: 864px;
    border-radius: 50%;
    background: var(--paper);
  }
  .greeting {
    position: absolute;
    left: 0;
    width: 811px;
    top: 256px;
    margin: 0;
    text-align: center;
    font-size: 31px;
    font-weight: 800;
    letter-spacing: 0.04em;
    white-space: nowrap;
  }
  .message {
    position: absolute;
    left: 149px;
    top: 338px;
    font-size: 15.5px;
    font-weight: 700;
    line-height: 30px;
    letter-spacing: 1px;
    white-space: nowrap;
  }
  .message p {
    margin: 0 0 46px;
  }
  .signature {
    position: absolute;
    left: 0;
    top: 632px;
    width: 811px;
    font-size: 15.5px;
    font-weight: 700;
    line-height: 31px;
    letter-spacing: 0.06em;
    white-space: nowrap;
  }
  .signature .company { padding-left: 284px; }
  .signature .officer { padding-left: 330px; }
  .signature .staff {
    padding-left: 680px;
    margin-top: 26px;
  }
  .horse-area {
    position: absolute;
    left: 108px;
    top: 752px;
    width: 450px;
    height: 350px;
  }
  .brand {
    position: absolute;
    left: 378px;
    top: 1118px;
    display: flex;
    align-items: center;
    gap: 16px;
    color: var(--paper);
    font-size: 23px;
    font-weight: 700;
    letter-spacing: 0.08em;
    white-space: nowrap;
  }
  .brand-dot {
    width: 28px;
    height: 28px;
    border-radius: 50%;
    background: var(--paper);
  }
</style>
</head>
<body>
<main class="card">
  <div class="sun"></div>

  <h1 class="greeting">明けましておめでとうございます。</h1>

  <div class="message">
    <p>創業以来四半世紀に及ぶ活動を礎に、<br>また新たな第一歩を踏み出しました。</p>
    <p>これからも、アグレッシブに、元気に、正しきことに労を惜しまず、<br>日々挑戦し続けます。</p>
    <p>本年も更に皆様のお役に立てる存在を目指し精進致します。</p>
  </div>

  <div class="signature">
    <div class="company">株式会社セキレイワークス</div>
    <div class="officer">代表取締役会長　○○○○</div>
    <div class="officer">代表取締役社長　○○○○</div>
    <div class="staff">社員一同</div>
  </div>

  <svg class="horse-area" viewBox="0 0 450 350" role="img" aria-label="Black silhouette of a rearing horse">
    <rect x="0" y="0" width="450" height="350" fill="var(--silhouette)"/>
  </svg>

  <div class="brand">
    <span class="brand-dot"></span>
    <span class="brand-name">SEKIREI WORKS INC.</span>
  </div>
</main>
</body>
</html>
```